Help Design the Packaging for our Nicotine Replacement Therapy

Packaging Design Brief for Brevora
We are using this contest to find a designer who can design the packaging for the full line of products listed below for our new brand. This contest will require you to provide designs for the Traditional mint in both the 2mg and 4mg, and the Traditional Cinnamon 2 mg and 4mg, plus the mint in the Modern, 2mg and 4mg. We would like to see how you propose to tie the designs together so their is clear differentiate between the products and flavors, yet it maintains brand cohesiveness.
We would like to then work with the contest winner on a 1-1 project to develop the packaging for the remaining products.
Project Overview:
Brevora is launching a new line of nicotine replacement therapy (NRT) products, including gum and lozenges in multiple flavors and strengths. The packaging design needs to reflect Brevora’s brand values of trust, warmth, professionalism, and customer-centricity while being visually appealing, functional, and easily distinguishable.
Here is our full product line up so you can design product packaging that has the potential to expand as we add more flavors.
Product Line-Up:
1. Nicotine Gum ("Traditional" because it tastes and feels like hollbeck's gum):
- Flavors: Mint, Fruit, Cinnamon
- Strengths: 2mg, 4mg
- Pack Size: 240 pieces per pack
2. Nicotine Gum (Stiffer, Playdough-Like Texture will be called "Classic"):
- Strengths: 2mg, 4mg
3. Nicotine Lozenges:
- Flavors: Mint, Citrus, Berry
- Strengths: 2mg, 4mg
- Pack Size: 120 pieces per pack
Design Objectives:
1. Brand Consistency:
- The Brevora logo should be easily recognizable across all packaging.
- The design should reflect the brand’s personality: trustworthy, professional, warm, and approachable.
- Packaging should evoke a sense of reliability and comfort, appealing to a mature audience.
2. Differentiation:
- Flavor Differentiation:
- Use distinct colors for each flavor to ensure they are easily distinguishable.
- Incorporate icons or images that represent the flavor (e.g., mint leaves for Mint, cinnamon sticks for Cinnamon).
- Strength Differentiation:
- Clearly display the nicotine strength (2mg or 4mg) in a way that stands out at a glance.
- Gum Texture Differentiation:
- Create a visual distinction between the traditional chewing gum and the stiffer, playdough-like gum while maintaining a cohesive brand look.
- Consider using different background textures, patterns, or additional design elements to indicate the different textures while ensuring they still feel part of the same family.
3. Product Type Differentiation:
- Gum vs. Lozenges:
- The lozenges should be visually distinct from the gum products while still fitting within the overall Brevora brand aesthetic.
- Consider using a different shape or design element on the lozenge packaging (e.g., a lozenge icon or a unique pattern) to differentiate them from the gum.
- Maintain consistent use of colors for flavors across both gum and lozenge packaging (e.g., Mint gum and Mint lozenges should share the same color scheme) to unify the product line.
4. Scalability:
- The design should be flexible enough to accommodate additional flavors or product variations in the future.
- Ensure that any new flavor or product type can be easily integrated into the existing design template.
Content Requirements:
1. Front of Pack:
- Brevora logo
- Flavor name and representative image
- Nicotine strength (2mg or 4mg)
- Indication of gum type (Traditional or Stiffer texture)
- Pack size (e.g., "240 Pieces")
2. Here are the die lines from the manufacturer. You will see that there are certain things that must be included on the gum packaging:
https://files.tarnowbox.net/folders/8qpe27Lm_X4v81ZsKd0n-WRyTa3GbU7Hc?usp=share_link
Overall Feel:
- The packaging should communicate that Brevora is a trustworthy, professional brand with a warm, supportive approach. It should feel modern and appeal to a broad audience both male and female.
Packaging design for all SKUs listed above, with clear differentiation between flavors, strengths, and product types.
Here is the link to the brevora logo. https://files.tarnowbox.net/file/d/7-RHbwPqJmm412LcuvzxAq3QWEtn5ZK9S/view?usp=sharing We are not opposed to the color of the dots and + sign changing to signify flavor either.
Target Market(s)
individuals 18-55+ looking to quit vaping and smoking
Industry/Entity Type
nicotine replacement therapy
Other font styles liked:
- should compliment and look good with our logo and font which is Nexa bold
Requirements
Must have
- we want to look professional and trustworthy. . .and we want a design that is cohesive across the product set and can expand and stay on brand with additional flavors.
Nice to have
- We will pick a winner and then pay that winner to do the rest of the package designs for each sku and lozenges too.

```html
<!DOCTYPE html>
<html lang="en">
<head>
<meta charset="UTF-8">
<title>Brevora Mint Lozenges – Label</title>
<link rel="stylesheet" href="https://fonts.googleapis.com/css2?family=Montserrat:wght@300;700;800&display=swap">
<style>
  :root {
    --plum: #8e4678;
    --plum-soft: #a0648c;
    --sage: #a9bfad;
    --sage-light: #b6c9b9;
    --ink: #111111;
    --page: #ffffff;
  }
  * { margin: 0; padding: 0; box-sizing: border-box; }
  html, body {
    width: 900px;
    height: 1200px;
    overflow: hidden;
    background: var(--page);
  }
  .canvas {
    position: relative;
    width: 900px;
    height: 1200px;
  }
  .label {
    position: absolute;
    left: 170px;
    top: 122px;
    width: 560px;
    height: 957px;
    overflow: hidden;
    box-shadow: 6px 8px 10px rgba(0,0,0,0.25);
    font-family: "Montserrat", Arial, sans-serif;
  }
  .label__pattern {
    position: absolute;
    inset: 0;
    background: radial-gradient(circle at 50% 51%, var(--sage-light) 0%, var(--sage) 30%, var(--plum-soft) 65%, var(--plum) 100%);
  }
  .type-tab {
    position: absolute;
    left: 178px;
    top: 0;
    width: 210px;
    height: 86px;
    background: var(--sage);
    border: 2px solid var(--plum);
    border-top: none;
    display: flex;
    flex-direction: column;
    align-items: center;
    justify-content: center;
    color: var(--plum);
    font-weight: 300;
    font-size: 21px;
    line-height: 1.2;
  }
  .type-tab::after {
    content: "";
    position: absolute;
    left: 6px; right: 6px; bottom: 6px;
    border-bottom: 2px solid var(--plum);
  }
  .hero {
    position: absolute;
    left: 92px;
    top: 301px;
    width: 376px;
    height: 376px;
    border-radius: 50%;
    background: var(--sage);
    display: flex;
    flex-direction: column;
    align-items: center;
    justify-content: center;
  }
  .brand {
    display: flex;
    align-items: center;
    gap: 10px;
    margin-top: 10px;
  }
  .brand__dot {
    width: 14px;
    height: 14px;
    border-radius: 50%;
    background: var(--ink);
  }
  .brand__name {
    color: var(--ink);
    font-weight: 800;
    font-size: 66px;
    letter-spacing: -1px;
    line-height: 1;
  }
  .flavor {
    margin-top: 16px;
    color: var(--plum);
    font-weight: 800;
    font-size: 26px;
    letter-spacing: 1px;
    text-align: center;
    line-height: 1.25;
  }
  .flavor__name {
    display: flex;
    align-items: center;
    gap: 12px;
  }
  .flavor__name::before,
  .flavor__name::after {
    content: "";
    width: 66px;
    border-top: 2px solid var(--plum);
  }
  .pack-count {
    position: absolute;
    left: 40px;
    bottom: 40px;
    color: var(--ink);
    font-weight: 800;
    text-align: center;
    line-height: 1;
  }
  .pack-count__number { display: block; font-size: 34px; }
  .pack-count__unit { display: block; font-size: 13px; letter-spacing: 0.5px; margin-top: 2px; }
  .strength {
    position: absolute;
    right: 38px;
    bottom: 46px;
    color: var(--ink);
    font-weight: 800;
    font-size: 31px;
  }
</style>
</head>
<body>
<main class="canvas">
  <section class="label">
    <div class="label__pattern" role="img" aria-label="Plum and sage swirl rays radiating from the centre, scattered with candy and mint leaf icons"></div>

    <div class="type-tab">
      <span>nicotine</span>
      <span>lozenges</span>
    </div>

    <div class="hero">
      <div class="brand">
        <span class="brand__dot"></span>
        <span class="brand__name">Brevora</span>
      </div>
      <div class="flavor">
        <span class="flavor__name">MINT</span>
        <span class="flavor__type">LOZENGES</span>
      </div>
    </div>

    <div class="pack-count">
      <span class="pack-count__number">120</span>
      <span class="pack-count__unit">MINTS</span>
    </div>
    <div class="strength">4MG</div>
  </section>
</main>
</body>
</html>
```